Tabloid Magazine Flyer Class Action Lawsuit

Create a bold, 2-page 8.5" x 11" flyer with the look and feel of a tabloid exposé — loud, sensational, and impossible to ignore. Use bold fonts, dramatic headlines, and high-contrast colors (red, black, white, deep blue). Fill every inch of space — no white space, no subtlety. Use the provided images prominently. Page 1 should grab attention with a shocking headline, impactful image, and strong call to action. Page 2 should stack bold subheadings and explosive bullet points. Emphasize urgency, outrage, and grassroots power. This flyer is meant to rally a community.
Updates

Need to extend because we haven't received a design that meets our needs

Target Market(s)

All instructions and content are in the attached word doc

Industry/Entity Type

Requirements
Must have
• All instructions and content are in the attached word doc
Nice to have
Should not have

```html
<!DOCTYPE html>
<html lang="en">
<head>
<meta charset="utf-8">
<title>Save Harborview Park – Community Flyer</title>
<link href="https://fonts.googleapis.com/css2?family=Montserrat:wght@500;600;700;800&display=swap" rel="stylesheet">
<style>
  :root {
    --backdrop: #cbcbcb;
    --paper: #ffffff;
    --blue: #1660a3;
    --red: #d03428;
    --red-dark: #c9302a;
    --ink: #111111;
  }
  * { box-sizing: border-box; margin: 0; padding: 0; }
  html, body { width: 1200px; height: 2258px; overflow: hidden; }
  body {
    background: var(--backdrop);
    font-family: "Montserrat", Arial, sans-serif;
    color: var(--ink);
    position: relative;
  }
  .page {
    position: absolute;
    left: 196px;
    width: 808px;
    height: 1044px;
    background: var(--paper);
  }
  .page--front { top: 78px; }
  .page--back { top: 1152px; }
  .abs { position: absolute; left: 0; right: 0; text-align: center; }

  .org-mark {
    display: flex; align-items: center; justify-content: center; gap: 14px;
  }
  .org-mark__dot {
    width: 46px; height: 46px; border-radius: 50%; background: var(--blue);
  }
  .org-mark__name {
    font-weight: 800; font-size: 34px; line-height: 1.05; color: var(--red);
    text-align: left; letter-spacing: -0.5px; text-transform: uppercase;
  }

  .headline-band {
    top: 203px; height: 153px; background: var(--blue); color: #fff;
    display: flex; flex-direction: column; justify-content: center;
    font-weight: 800; font-size: 32px; line-height: 1.2;
  }
  .rally { top: 372px; font-weight: 700; font-size: 21px; }
  .ownership { top: 440px; font-weight: 700; font-size: 15px; line-height: 1.3; }
  .invite { top: 502px; color: var(--blue); font-weight: 700; }
  .invite__lead { font-size: 21px; }
  .invite__meeting { font-size: 26px; font-weight: 800; line-height: 1.3; }
  .event { top: 586px; color: var(--red); font-weight: 800; }
  .event__date { font-size: 32px; line-height: 1.2; }
  .event__place { font-size: 17px; font-weight: 700; }
  .cta-box {
    left: 109px; right: 109px; top: 664px; height: 177px;
    background: var(--blue); color: #fff;
    display: flex; flex-direction: column; justify-content: center;
    font-weight: 800; font-size: 29px; line-height: 1.25;
  }
  .lawsuit { top: 858px; font-size: 16px; line-height: 1.22; font-weight: 500; }
  .lawsuit strong { font-weight: 700; display: block; }
  .site-link { top: 968px; color: var(--red); font-weight: 800; font-size: 30px; }

  .expose-intro {
    top: 195px; left: 64px; right: 64px; font-size: 12.5px; line-height: 1.3; font-weight: 500;
  }
  .expose-intro strong { font-weight: 700; }
  .facts {
    position: absolute; left: 21px; right: 21px; top: 272px; height: 606px;
    background: var(--red-dark); color: #fff; padding: 22px 30px 0;
  }
  .facts__title { font-weight: 800; font-size: 21px; margin-bottom: 18px; }
  .fact { margin-bottom: 17px; font-size: 12.6px; line-height: 1.27; font-weight: 500; }
  .fact__head { font-weight: 700; display: block; }
  .closing { top: 894px; color: var(--blue); font-weight: 800; font-size: 22px; line-height: 1.25; }
</style>
</head>
<body>

<section class="page page--front">
  <div class="abs org-mark" style="top:66px">
    <span class="org-mark__dot"></span>
    <span class="org-mark__name">Access Equals<br>Justice Coalition</span>
  </div>

  <div class="abs headline-band">
    <span>HARBORVIEW PARK EXPOSED</span>
    <span>DISABLED CHILD TRAUMATIZED</span>
    <span>PUBLIC LAND ABUSED FOR PROFIT</span>
  </div>

  <p class="abs rally">HELP OUR BEACH COMMUNITY FIGHT BACK</p>
  <p class="abs ownership">HARBORVIEW PARK IS NOT PRIVATE. IT IS PUBLIC PROPERTY<br>OWNED BY THE CITY, PAID FOR BY YOU.</p>

  <div class="abs invite">
    <p class="invite__lead">JOIN us &amp; SHOW YOUR SUPPORT @</p>
    <p class="invite__meeting">SEACLIFF BEACH TOWN COUNCIL MEETING</p>
  </div>

  <div class="abs event">
    <p class="event__date">Date: May 14, 2025 – 6:00 PM</p>
    <p class="event__place">Place: Harborview Park Community Room (Above the Arcade)</p>
  </div>

  <div class="abs cta-box">
    <span>HELP OUR COMMUNITY SAVE</span>
    <span>HARBORVIEW PARK</span>
    <span>HARBORVIEW PARK WAS BUILT FOR</span>
    <span>FAMILIES — NOT RAVES</span>
  </div>

  <p class="abs lawsuit">
    <strong>CLASS ACTION LAWSUIT FORMING NOW!</strong>
    If you’ve been impacted by noise, denied public access, or harmed<br>
    by these violations, you may be eligible for compensation.<br>
    We’re gathering stories and preparing legal action.
  </p>

  <p class="abs site-link">www.SaveHarborviewPark.org</p>
</section>

<section class="page page--back">
  <div class="abs org-mark" style="top:70px">
    <span class="org-mark__dot"></span>
    <span class="org-mark__name">Access Equals<br>Justice Coalition</span>
  </div>

  <p class="abs expose-intro"><strong>EXPOSED: Marco Venturi</strong>, CEO of Meridian Asset Holdings IV LLC the leaseholder of Harborview Park, has drawn community outrage for profiting off public land while operating Harborview Park in ways many say violate its lease and damage our beach, our peace, and our environment — all from his luxury estate in Oak Hollow.</p>

  <div class="facts">
    <h2 class="facts__title">WHAT THEY DON’T WANT YOU TO KNOW:</h2>
    <p class="fact"><span class="fact__head">ILLEGAL RAVES – NO PERMITS.</span>Explosive concerts over 100 decibels, blasting Seacliff Beach with bass — multiple times per week. According to Public Records these events had NO PERMITS &amp; NO CITY APPROVAL.</p>
    <p class="fact"><span class="fact__head">THE SHORE CLUB ISN’T THEIRS – IT’S YOURS.</span>Harborview Park is shutting down public space for 9 private Shore Club raves through July. But July 5 is different — “Liberty Fest” is a full-park, alcohol-fueled rave that shuts out the public from taxpayer-owned land. These takeovers appear to violate their lease and Prop G, which protects YOUR beach for ALL — not just paying partiers.</p>
    <p class="fact"><span class="fact__head">DISABLED CHILD TRAUMATIZED BY RAVE NOISE</span>A child with cerebral palsy and auditory sensitivity came to use the City’s Beach Accessibility Program but was overwhelmed by deafening Rave noise and fled in distress. The illegal sound levels deny All individuals with similar disabilities access to public accommodations. This is a direct violation of the Americans with Disabilities Act.</p>
    <p class="fact"><span class="fact__head">EXPOSED: IS HARBORVIEW RUNNING AN UNETHICAL SELF-DEALING SCHEME ?</span>Harborview Park’s General Manager, Glen Harper, is also CEO of Shoreline Guard Services — the very company hired by Harborview for “security” services. And who’s listed as corporate secretary? Carla Venturi, close relative of the leaseholder Marco Venturi. Is this Self-Dealing?</p>
    <p class="fact"><span class="fact__head">DOCUMENTED RUNOFF AND SUSPECTED ENVIRONMENTAL DISASTER</span>Improperly Stored Chemicals, oils, and waste water spilling into storm drains. Parking lots are trashed, flooded, and neglected. Stormwater compliance appears to be ignored.</p>
    <p class="fact"><span class="fact__head">EXPOSED: HARBORVIEW PARK’S ILLEGAL SIGNS MISLEAD THE PUBLIC.</span>They’re tricking the public into believing city-owned land is private, violating their lease which requires signage clearly stating the property is city-owned and open to all.</p>
    <p class="fact"><span class="fact__head">HARBORVIEW PARK: ACCIDENT WAITING TO HAPPEN?</span>From the Thunder Coaster to the rides and walkways, safety appears ignored. The lease requires independent engineer inspections — yet no reports can be found. With what looks like hundreds of code violations, the entire park may be one broken bolt from disaster. Who’s protecting the public?</p>
  </div>

  <p class="abs closing">HELP OUR COMMUNITY SAVE HARBORVIEW PARK<br>HARBORVIEW PARK WAS BUILT FOR FAMILIES — NOT RAVES</p>

  <p class="abs site-link">www.SaveHarborviewPark.org</p>
</section>

</body>
</html>
```